Netvale - Seafood industry professional promoting page

Hi. I´m in the seafood business with a one man company sourcing and exporting frozen seafood. I need to make a one page homepage for Netvale (from Iceland). The feeling of it should be; Trustworthy, experience and knowledge.
Using as background a picture (or part of it), or a moving video:

http://www1.bryla.is/vefur/myndir/lysingur.jpg
https://clipvault.example/583027416

Main text to be:

- We can help source, market and add value to your seafood business
- Years of experience in seafood trade and production
- Extensive knowledge of fishing, seasonality, production and accreditations

Contact:
torvi@netvale.is
Tel: +3654172093
(with a photo)

p.s. please also make logo look better.

Target Market(s)

Seafood industry

Industry/Entity Type

Business

Logo Text

Netvale

Coding

Coded - Design and coding required

Number of Pages Required

1 page

Colors
0792cd
33a6d7

```html
<!DOCTYPE html>
<html lang="en">
<head>
<meta charset="utf-8">
<title>Netvale – Seafood sourcing and export</title>
<link rel="stylesheet" href="https://fonts.googleapis.com/css2?family=Open+Sans:wght@300;400;600;700&display=swap">
<style>
  :root {
    --brand-blue: #0792cd;
    --brand-blue-light: #33a6d7;
    --bar-dark: #2b2b2d;
    --header-white: #f4f4f4;
    --text-dark: #555a60;
    --text-light: #ffffff;
    --hero-base: #c9cbcf;
    --hero-warm: #b0654f;
    --hero-cool: #8e9aa6;
    --band-end: #dfe9f3;
  }
  * { box-sizing: border-box; margin: 0; padding: 0; }
  html, body {
    width: 1200px; height: 857px; overflow: hidden;
    background: #ffffff;
    font-family: "Open Sans", Arial, sans-serif;
  }
  .page { position: relative; width: 1200px; height: 857px; }

  .accent-strip { height: 14px; background: var(--brand-blue); }

  .top-bar {
    height: 48px; background: var(--bar-dark); color: var(--text-light);
    display: flex; align-items: center; padding: 0 24px; font-size: 13px;
  }
  .top-bar .contact-item { display: flex; align-items: center; gap: 8px; }
  .top-bar .contact-item b { font-weight: 700; }
  .top-bar .contact-item span { color: #cfd2d6; }
  .top-bar .phone { width: 360px; }
  .top-bar .social { margin-left: auto; display: flex; align-items: center; gap: 14px; font-weight: 700; }
  .social .dot { width: 11px; height: 11px; border-radius: 50%; background: var(--text-light); }

  .site-header {
    height: 66px; background: var(--header-white);
    display: flex; align-items: center; padding: 0 24px;
  }
  .wordmark { font-size: 28px; font-weight: 300; color: var(--text-dark); letter-spacing: 1px; text-transform: uppercase; }
  .main-nav { margin-left: auto; display: flex; gap: 34px; }
  .main-nav a {
    text-decoration: none; font-size: 12px; font-weight: 700;
    color: var(--text-dark); text-transform: uppercase; letter-spacing: .5px;
  }
  .main-nav a.active { color: var(--brand-blue); }

  .hero { position: relative; height: 500px; overflow: hidden; }
  .hero-photo {
    position: absolute; inset: 0;
    background:
      radial-gradient(ellipse at 22% 25%, var(--hero-warm) 0%, transparent 38%),
      radial-gradient(ellipse at 55% 75%, #b55a55 0%, transparent 30%),
      radial-gradient(ellipse at 80% 50%, var(--hero-cool) 0%, transparent 45%),
      linear-gradient(120deg, #d7d5d2 0%, var(--hero-base) 50%, #a9b1ba 100%);
  }
  .hero-shade { position: absolute; inset: 0; background: rgba(0,0,0,.18); }
  .hero-copy { position: absolute; left: 150px; top: 120px; color: var(--text-light); width: 560px; }
  .hero-copy h1 { font-size: 27px; font-weight: 400; line-height: 1.25; }
  .hero-copy p { font-size: 14px; margin-top: 10px; }
  .btn-start {
    display: inline-block; margin-top: 34px; padding: 13px 22px;
    border: 2px solid var(--text-light); color: var(--text-light);
    font-size: 12px; font-weight: 700; text-transform: uppercase; text-decoration: none;
  }
  .hero-brand {
    position: absolute; left: 790px; top: 90px;
    display: flex; flex-direction: column; align-items: center; gap: 8px;
  }
  .hero-brand .mark-circle { width: 62px; height: 62px; border-radius: 50%; background: var(--brand-blue-light); }
  .hero-brand .brand-name { font-size: 30px; font-weight: 700; color: var(--brand-blue); line-height: 1.1; }

  .footer-band {
    height: 229px;
    background: linear-gradient(160deg, var(--brand-blue) 0%, var(--brand-blue-light) 45%, var(--band-end) 100%);
  }
</style>
</head>
<body>
<div class="page">
  <div class="accent-strip"></div>

  <div class="top-bar">
    <div class="contact-item phone">
      <svg width="12" height="12" viewBox="0 0 24 24" aria-hidden="true"><path fill="#fff" d="M6.6 10.8a15.1 15.1 0 0 0 6.6 6.6l2.2-2.2c.3-.3.7-.4 1-.2 1.1.4 2.3.6 3.6.6.6 0 1 .4 1 1V20c0 .6-.4 1-1 1A17 17 0 0 1 3 4c0-.6.4-1 1-1h3.5c.6 0 1 .4 1 1 0 1.3.2 2.5.6 3.6.1.3 0 .7-.2 1z"/></svg>
      <b>Phone</b><span>+3654172093</span>
    </div>
    <div class="contact-item email">
      <svg width="13" height="10" viewBox="0 0 26 20" aria-hidden="true"><rect x="1" y="1" width="24" height="18" fill="none" stroke="#fff" stroke-width="2"/><path d="M1 1l12 10L25 1" fill="none" stroke="#fff" stroke-width="2"/></svg>
      <b>Email</b><span>torvi@netvale.is</span>
    </div>
    <div class="social">
      Meet us on
      <span class="dot"></span><span class="dot"></span><span class="dot"></span><span class="dot"></span>
    </div>
  </div>

  <header class="site-header">
    <div class="wordmark">Netvale</div>
    <nav class="main-nav">
      <a class="active" href="#home">Home</a>
      <a href="#about">About</a>
      <a href="#team">Team</a>
      <a href="#service">Service</a>
      <a href="#gallery">Gallery</a>
      <a href="#contact">Contact</a>
    </nav>
  </header>

  <section class="hero" id="home">
    <div class="hero-photo" role="img" aria-label="Fresh seafood laid out: crab, prawns, red fish and whole cod on ice"></div>
    <div class="hero-shade"></div>
    <div class="hero-brand">
      <span class="mark-circle"></span>
      <span class="brand-name">Netvale</span>
    </div>
    <div class="hero-copy">
      <h1>"We can help source, market and add value to your seafood business</h1>
      <p>- Extensive knowledge of fishing</p>
      <a class="btn-start" href="#about">Get started</a>
    </div>
  </section>

  <div class="footer-band"></div>
</div>
</body>
</html>
```